Back Pain

Need a flyer similar to the attached draft. This is to be handed out to prospective patients. Note that Sketch Hive has already designed the logo. If you need a copy please contact me

```html
<!DOCTYPE html>
<html lang="en">
<head>
<meta charset="utf-8">
<title>Tech Neck – Spine Ease Clinic Flyer</title>
<link href="https://fonts.googleapis.com/css2?family=Montserrat:wght@300;400;500;600;700;800&family=Cabin:wght@400;600;700&display=swap" rel="stylesheet">
<style>
  :root{
    --blue:#1b75bc;
    --green:#8dc63f;
    --charcoal:#3a3a3c;
    --white:#ffffff;
    --ink:#111111;
    --photo-light:#eceef0;
    --photo-mid:#b9b7ae;
    --photo-dark:#5c5f58;
  }
  *{margin:0;padding:0;box-sizing:border-box}
  html,body{width:849px;height:1200px;overflow:hidden;background:var(--white)}
  .flyer{position:relative;width:849px;height:1200px;background:var(--white);font-family:"Montserrat",sans-serif;overflow:hidden}
  .abs{position:absolute}
  .photo-area{left:0;top:0;width:431px;height:787px;
    background:linear-gradient(180deg,var(--photo-light) 0%,var(--photo-light) 30%,var(--photo-mid) 55%,var(--photo-dark) 75%,var(--photo-dark) 100%)}
  .info-panel{left:431px;top:0;width:418px;height:787px;background:var(--charcoal)}
  .title{top:44px;font-weight:800;font-size:90px;line-height:1;letter-spacing:-4px}
  .title-tech{left:166px;color:var(--blue)}
  .title-neck{left:455px;color:var(--green)}
  .chart{left:0;top:0}
  .divider{left:448px;width:363px;height:1.5px;background:var(--white)}
  .stat-text{left:548px;color:var(--white);text-transform:uppercase;white-space:nowrap}
  .stat-lead{top:541px;font-size:14.5px;font-weight:400}
  .stat-figure{top:559px;font-size:24px;font-weight:600;color:var(--green)}
  .stat-tail{top:590px;font-size:14.5px;font-weight:400}
  .symptoms{list-style:none;color:var(--white);font-weight:600;font-size:16px;white-space:nowrap}
  .symptoms li{height:32px;line-height:20px}
  .symptoms li::before{content:"\2192";margin-right:4px;font-weight:700}
  .symptoms-left{left:459px;top:667px}
  .symptoms-right{left:690px;top:667px}
  .message-band{left:0;top:795px;width:849px;height:107px;background:var(--green);
    font-family:"Cabin",sans-serif;font-size:25px;color:var(--ink);text-align:center;line-height:34px;padding-top:18px}
  .message-band strong{font-weight:700}
  .contact-panel{left:431px;top:912px;width:418px;height:288px;background:var(--charcoal);color:var(--white)}
  .brand-mark{left:161px;top:972px;width:138px;height:138px;border-radius:50%;background:var(--blue)}
  .brand-name{left:0;width:454px;top:1116px;text-align:center;font-weight:600;font-size:31px;color:var(--blue);letter-spacing:-0.5px;white-space:nowrap}
  .doctor{left:447px;top:945px;font-size:25px;font-weight:600;white-space:nowrap}
  .doctor .first{color:var(--blue)}
  .doctor .last{color:var(--green)}
  .location{left:447px;top:975px;font-size:14px;font-weight:300;color:var(--white);line-height:22px}
  .location b,.booking b{font-weight:600}
  .offer-rule{left:441px;width:342px;height:1.5px;background:var(--white)}
  .offer{left:447px;top:1050px;font-size:18.5px;font-weight:600;color:var(--white);white-space:nowrap}
  .offer .discount{color:var(--blue)}
  .booking{left:447px;top:1101px;font-size:14px;font-weight:300;color:var(--white);line-height:22px}
</style>
</head>
<body>
<main class="flyer">
  <div class="abs photo-area" role="img" aria-label="Photo of a woman from behind holding her sore neck and shoulder"></div>
  <section class="abs info-panel"></section>

  <h1 class="abs title title-tech">TECH</h1>
  <h1 class="abs title title-neck">NECK</h1>

  <svg class="abs chart" width="849" height="787" viewBox="0 0 849 787" aria-label="Bar chart of pressure on spine by degree of forward head tilt">
    <defs>
      <linearGradient id="barFill" x1="0" y1="0" x2="0" y2="1">
        <stop offset="0" stop-color="#1b75bc"/>
        <stop offset="1" stop-color="#8dc63f"/>
      </linearGradient>
    </defs>
    <g font-family="Montserrat, sans-serif" font-size="11" fill="#ffffff">
      <text x="462" y="171">As the Head Tilts Forward.</text>
      <text x="462" y="189">More Force is placed on the Spine</text>
    </g>
    <rect x="461" y="210" width="67" height="69" fill="#8a8a8c" role="img" aria-label="Side profile icon of a head tilting forward"/>
    <g>
      <rect x="462" y="364" width="43" height="48" fill="url(#barFill)"/>
      <rect x="527" y="298" width="43" height="114" fill="url(#barFill)"/>
      <rect x="592" y="237" width="43" height="175" fill="url(#barFill)"/>
      <rect x="658" y="205" width="43" height="207" fill="url(#barFill)"/>
      <rect x="722" y="159" width="43" height="253" fill="url(#barFill)"/>
    </g>
    <g font-family="Montserrat, sans-serif" font-weight="600" font-size="13" fill="#ffffff" text-anchor="middle">
      <text x="483" y="381">12</text>
      <text x="548" y="315">27</text>
      <text x="613" y="254">40</text>
      <text x="679" y="222">49</text>
      <text x="743" y="176">60</text>
      <text x="488" y="437">0˚</text>
      <text x="549" y="437">15˚</text>
      <text x="612" y="437">30˚</text>
      <text x="680" y="437">45˚</text>
      <text x="743" y="437">60˚</text>
    </g>
    <text x="617" y="463" font-family="Montserrat, sans-serif" font-size="13.5" fill="#ffffff" text-anchor="middle">Degrees of Forward Head Tilt</text>
    <text transform="translate(795 287) rotate(-90)" font-family="Montserrat, sans-serif" font-size="13.5" fill="#ffffff" text-anchor="middle">Pressure on Spine (LBS)</text>
    <g transform="translate(496 574)">
      <circle r="41" fill="#ffffff"/>
      <path d="M0 0 L0 -41 A41 41 0 0 1 23.5 33.6 Z" fill="#8dc63f"/>
    </g>
  </svg>

  <div class="abs divider" style="top:536px;top:511px"></div>
  <p class="abs stat-text stat-lead">The average person spends</p>
  <p class="abs stat-text stat-figure">8-11 Hours per day</p>
  <p class="abs stat-text stat-tail">Using electronic devices</p>
  <div class="abs divider" style="top:627px"></div>

  <ul class="abs symptoms symptoms-left">
    <li>HEADACHES</li>
    <li>SHOULDER PAIN</li>
    <li>ARM &amp; HANDPAIN</li>
  </ul>
  <ul class="abs symptoms symptoms-right">
    <li>NECK PAIN</li>
    <li>BACK PAIN</li>
    <li>SCIATICA</li>
  </ul>

  <section class="abs message-band">
    <p><strong>Chiropractic Care</strong> can help Correct and Prevent these problems</p>
    <p>by <strong>Restoring</strong> and <strong>Maintaining Proper Alingment</strong> of the <strong>Neck</strong></p>
  </section>

  <div class="abs brand-mark" aria-hidden="true"></div>
  <p class="abs brand-name">SPINE EASE CLINIC</p>

  <section class="abs contact-panel"></section>
  <h2 class="abs doctor"><span class="first">DR MARTIN</span> <span class="last">HALE</span></h2>
  <p class="abs location">Now in <b>Fremantle</b> at<br>42 Harbour Rd - Quay Suites</p>
  <div class="abs offer-rule" style="top:1044px"></div>
  <p class="abs offer"><span class="discount">50% OFF</span> INITIAL CONSULTATION</p>
  <div class="abs offer-rule" style="top:1078px"></div>
  <p class="abs booking">If you Book online at<br><b>www.spineeaseclinic.example</b><br>choose “<b>Tech Neck</b>” Option</p>
</main>
</body>
</html>
```